The Quiet Ladder Out of the Screen Trap - Contemporary Book Cover Design

The Quiet Ladder Out of the Screen Trap was published in March 2019 and is available on Brindlemart and other platforms now. However, I am not happy with the cover.  It's a good design in some ways - I thought it would stand out and be easily recognizable. But I don't really like the color scheme and feel that a self-help book should probably use some lighter colors and that the red is too strident. The color scheme carries over into other marketing materials like the website, social media, etc. and I don't like the red and black scheme for these purposes.
It's not essential that the cover contain an endorsement like the current one but it could. Here are some endorsements:
“A must-read for anyone who is addicted to or thinks they may have a problem with digital technology. This eloquent work will also be useful to academics and clinicians exploring potential solutions. The author recognizes the similarities between smartphone addiction and other addictions, and logically applies one of the most effective known solutions for addiction - The Quiet Ladder.”
-- Duncan Pellworth: Noted Interventionist, Keynote Speaker and Addiction Visionary
“If you suffer from digital addiction, I strongly encourage you to use this book as your road map to get you back to the real world.”
-- Gregory Tamsett, Founder of Feedline Review Weekly.
The back cover would have the new design / color scheme, but can have similar text, bio, author image, etc. Or we could include the endorsements there and shorten the other text.
As for the cover it could be stylized, or an image, a partial image, or whatever. I am open to suggestions. Think about what would be inviting for a person searching for help with moderating their smartphone use.
Let's add a subtitle as well "An Inner Journey Toward Balanced Device Habits"
Here is a link to the book:
https://www.brindlemart-books.example/Quiet-Ladder-Screen-Trap/dp/4820193766

Target Market(s)
General, since this issue affects almost everyone.
Colors
Designer to choose colors to be used in the design.
Look and feel

```html
<!DOCTYPE html>
<html lang="en">
<head>
<meta charset="utf-8">
<title>The Quiet Ladder Out of the Screen Trap – Cover</title>
<link rel="stylesheet" href="https://fonts.googleapis.com/css2?family=Bebas+Neue&family=Oswald:wght@500&display=swap">
<style>
  :root {
    --page-bg: #ffffff;
    --sky-top: #1f57a6;
    --sky-mid: #3b7fd0;
    --haze: #8fb6e6;
    --stairs: #1d4379;
    --stairs-deep: #122c55;
    --title-white: #ffffff;
    --title-yellow: #ffd21a;
  }
  * { margin: 0; padding: 0; box-sizing: border-box; }
  html, body {
    width: 1200px;
    height: 1200px;
    overflow: hidden;
    background: var(--page-bg);
  }
  .canvas {
    width: 1200px;
    height: 1200px;
    display: flex;
    align-items: center;
    justify-content: center;
  }
  .book-cover {
    position: relative;
    width: 740px;
    height: 1110px;
    overflow: hidden;
    text-align: center;
    font-family: "Bebas Neue", "Oswald", sans-serif;
  }
  .cover-scene {
    position: absolute;
    inset: 0;
    background:
      linear-gradient(160deg, transparent 0 52%, var(--stairs) 52.3%, var(--stairs-deep) 100%),
      radial-gradient(ellipse 70% 22% at 40% 62%, var(--haze) 0%, transparent 70%),
      linear-gradient(180deg, var(--sky-top) 0%, var(--sky-mid) 48%, var(--stairs) 100%);
  }
  .cover-title {
    position: relative;
    padding-top: 70px;
    line-height: 0.9;
    text-shadow: 0 3px 8px rgba(0, 20, 60, 0.35);
  }
  .title-small {
    display: block;
    font-size: 58px;
    color: var(--title-white);
  }
  .title-main {
    display: block;
    font-size: 136px;
    color: var(--title-white);
  }
  .title-accent {
    display: block;
    font-size: 176px;
    color: var(--title-yellow);
  }
  .cover-subtitle {
    position: relative;
    margin-top: 28px;
    font-family: "Oswald", sans-serif;
    font-weight: 500;
    font-size: 31px;
    color: var(--title-white);
    letter-spacing: 0.5px;
    text-shadow: 0 2px 6px rgba(0, 20, 60, 0.4);
  }
  .cover-subtitle .highlight { color: var(--title-yellow); }
  .cover-author {
    position: absolute;
    left: 0;
    right: 0;
    bottom: 70px;
    font-size: 104px;
    letter-spacing: 6px;
    color: var(--title-white);
    text-shadow: 0 3px 10px rgba(0, 10, 40, 0.5);
  }
</style>
</head>
<body>
  <main class="canvas">
    <article class="book-cover">
      <div class="cover-scene" role="img" aria-label="Dusk photograph of young people sitting apart on a long outdoor staircase, each looking down at a phone, under a blue sky"></div>
      <h1 class="cover-title">
        <span class="title-small">The</span>
        <span class="title-main">Quiet Ladder</span>
        <span class="title-small">Out of the</span>
        <span class="title-accent">Screen</span>
        <span class="title-accent">Trap</span>
      </h1>
      <p class="cover-subtitle">An <span class="highlight">Inner Journey</span> Toward Balanced Device Habits</p>
      <p class="cover-author">Martin Halvery</p>
    </article>
  </main>
</body>
</html>
```